Pharmaceutical Manufacturing Services Advertisement

We need a new full page advertisement designed for publication in international magazines. We are a custom pharmaceutical manufacturing company and we help biotechnology companies scale up their drug development for clinical trials. The products we help manufacture are therapeutics for global healthcare problems.

Target Market(s)

Verane Bio is a privately owned contract development manufacturing organisation (CDMO) headquartered in Kellow, QLD, Australia.

Our mission is to is to be a global leader in development and in the provision of contract manufacturing for active pharmaceutical ingredient processes.

Why we do what we Do:

To help advance Biotechnology Companies so that they can deliver innovative therapeutics
~ enabling patients to live longer, healthier and happier lives
~ which solves worldwide health problems

Verane Bio’s role is to develop, implement and scale up the production to deliver biologic medicines for patients in partnership with the biotechnology companies.

Industry/Entity Type

Biotechnology

Font styles to use
Sans Serif

Colors

Designer to choose colors to be used in the design.

Requirements
Must have
• Please see the script on the Word document. There are 4 optional Header Taglines. Additional ideas for multiple designs for the taglines welcomed.
• However preference is for either of the first two:
• 1. Building your vision for better healthcare
• 2. Bridging your vision for better healthcare
• File Specs:
• • All artwork should be submitted as high-resolution (300 min. dpi), press-ready PDF files
• • CMYK color only
• • Full page 8.25” x 10.812”; 209.55 x 274.62 mm
• • Live Area for all sizes: 0.25” (6.35 mm) inside the trim
• • Bleed Area for all sizes: Extends 0.125” (3.175 mm) from trim
Nice to have
• Modern Science look to inspire biotechnology companies to work with us.
• Search for images to use by keyword "recombinant dna"

```html
<!DOCTYPE html>
<html lang="en">
<head>
<meta charset="utf-8">
<title>Verane Bio – Building Your Vision for Better Healthcare</title>
<link href="https://fonts.googleapis.com/css2?family=Oswald:wght@600&family=Lato:ital,wght@0,400;0,700;0,900;1,700&family=Roboto+Condensed:wght@400&display=swap" rel="stylesheet">
<style>
  :root{
    --navy:#1f5a86;
    --band-blue:#1d5e8c;
    --lime:#c2d125;
    --ink:#2a2a2a;
    --grey:#6d6f72;
    --white:#ffffff;
    --frame:#c9c9c9;
  }
  *{margin:0;padding:0;box-sizing:border-box}
  html,body{width:916px;height:1200px;overflow:hidden;background:var(--white)}
  .page{position:relative;width:916px;height:1200px;border:1px solid var(--frame);overflow:hidden;font-family:"Lato",sans-serif;color:var(--ink)}
  .headline-band{position:absolute;left:0;top:79px;width:566px;height:66px}
  .headline-band svg{position:absolute;inset:0}
  .headline{position:absolute;left:53px;top:92px;font-family:"Oswald",sans-serif;font-weight:600;font-size:30px;letter-spacing:.6px;color:var(--navy);line-height:40px;transform:scaleX(.78);transform-origin:left center;white-space:nowrap}
  .brand{position:absolute;left:613px;top:66px;width:260px}
  .brand-name{font-family:"Lato",sans-serif;font-weight:900;font-size:41px;color:var(--navy);letter-spacing:.5px;line-height:50px;white-space:nowrap}
  .brand-sub{font-family:"Roboto Condensed",sans-serif;font-size:15px;color:var(--grey);letter-spacing:.2px;margin-top:12px;white-space:nowrap}
  .hero{position:absolute;left:0;top:164px;width:916px;height:610px;background:linear-gradient(120deg,#dfe9f6 0%,#9bb7dc 35%,#4d77ad 65%,#1e2f4f 100%)}
  .sub-band{position:absolute;left:0;top:774px;width:916px;height:58px}
  .sub-band svg{position:absolute;inset:0}
  .subhead{position:absolute;right:27px;top:786px;font-weight:700;font-style:italic;font-size:24.5px;color:var(--lime);white-space:nowrap}
  .intro{position:absolute;left:28px;top:856px;width:485px;font-size:15px;line-height:34px;text-align:justify}
  .intro p+p{margin-top:18px}
  .offer{position:absolute;left:547px;width:341px}
  .offer h2{background:var(--lime);height:16px;font-size:14px;font-weight:700;letter-spacing:2.2px;line-height:17px;padding-left:7px;color:#2b2b2b}
  .offer ul{list-style:none;margin-top:3px}
  .offer li{font-size:15px;line-height:18.5px;padding-left:24px;position:relative}
  .offer li::before{content:"";position:absolute;left:8px;top:7px;width:5px;height:5px;border-radius:50%;background:var(--ink)}
  .products{top:861px}
  .services{top:972px}
  .contact{position:absolute;left:547px;top:1093px;width:341px;height:79px;background:var(--band-blue);color:var(--white);font-weight:700;font-size:17.5px;line-height:22px;padding:5px 0 0 19px;letter-spacing:.3px;font-style:normal}
</style>
</head>
<body>
<div class="page">
  <div class="headline-band">
    <svg width="566" height="66" viewBox="0 0 566 66"><polygon points="0,0 566,0 540,66 0,66" fill="var(--lime)"/></svg>
  </div>
  <h1 class="headline">BUILDING YOUR VISION FOR BETTER HEALTHCARE</h1>

  <div class="brand">
    <div class="brand-name">VERANE BIO</div>
    <div class="brand-sub">BIOPHARMACEUTICAL MANUFACTURING</div>
  </div>

  <div class="hero" role="img" aria-label="Three scientists in lab coats and safety glasses examining green liquid in flasks, overlaid with white molecular hexagon lines"></div>

  <div class="sub-band">
    <svg width="916" height="58" viewBox="0 0 916 58"><polygon points="261,0 916,0 916,58 284,58" fill="var(--band-blue)"/></svg>
  </div>
  <p class="subhead">Your Partner in Early Phase Clinical Biomanufacturing</p>

  <div class="intro">
    <p>We have been serving the pharmaceutical, biotechnology and veterinary industry for over 20 years so you can create innovative medicines for worldwide health problems.</p>
    <p>Get your therapeutics to the patient faster with cost-effective manufacturing for your GMP clinical trial material. We offer rapid technology transfer, scale-up development and manufacturing of microbial cell-derived proteins at up to 500L scale. We prepare your active pharmaceutical ingredient (API) products to a world class standard ready for clinical development.</p>
  </div>

  <section class="offer products">
    <h2>PRODUCTS:</h2>
    <ul>
      <li>Recombinant proteins</li>
      <li>Live Biotherapeutics</li>
      <li>Bacterial vaccines</li>
      <li>Plasmid DNA</li>
    </ul>
  </section>

  <section class="offer services">
    <h2>SERVICES:</h2>
    <ul>
      <li>Bacterial / Yeast Fermentation</li>
      <li>Cell Banking</li>
      <li>Process Development/Scale-up</li>
      <li>cGMP Manufacture of biopharmaceutical APIs</li>
      <li>Stability Testing</li>
    </ul>
  </section>

  <address class="contact">
    Visit veranebio.com.au<br>
    Australia +61(7)30005182<br>
    Email enquiries@veranebio.com.au
  </address>
</div>
</body>
</html>
```